Landing Page IT Security Vendor

We need a landing page that uses our colour scheme (www.brantowguard.example). We created a draft (see attached). We do not need standard stock template design pages. Please only apply if you can design pages from scratch and try to be as close as possible to our draft. It is ok to also purchase commecrial stock pictures

Coding

Coded - Design and coding required

Number of Pages Required

1 page

```html
<!DOCTYPE html>
<html lang="en">
<head>
<meta charset="utf-8">
<title>Kestrel – Security Awareness Training</title>
<link rel="stylesheet" href="https://fonts.googleapis.com/css2?family=Rajdhani:wght@600;700&family=Raleway:wght@400;500;600;700&display=swap">
<style>
:root{
  --teal:#16b5c2;
  --teal-dark:#0fb3c0;
  --yellow:#fdb531;
  --orange:#f9a51a;
  --ink:#2b2b2b;
  --dark:#393939;
  --text:#3a3a3a;
  --muted:#555;
  --soft:#f6f8fb;
  --line:#d9dde2;
  --white:#fff;
}
*{box-sizing:border-box;margin:0;padding:0}
html,body{width:1200px;height:2823px;overflow:hidden}
body{position:relative;background:var(--white);font-family:"Raleway",sans-serif;color:var(--text)}
.display{font-family:"Rajdhani",sans-serif;font-weight:700;letter-spacing:.5px}

/* hero */
.hero{position:absolute;left:0;top:0;width:1200px;height:631px;overflow:hidden}
.hero-photo{position:absolute;left:520px;top:0;width:680px;height:631px;
  background:radial-gradient(circle at 70% 35%,#4a4fd6 0%,#3b2a9a 35%,#2a1a5c 70%,#1c1238 100%)}
.hero-mask{position:absolute;left:0;top:0}
.brand{position:absolute;left:148px;top:38px;display:flex;align-items:center;gap:8px;
  font-family:"Rajdhani",sans-serif;font-weight:700;font-size:28px;line-height:36px;color:var(--ink)}
.brand-dot{width:30px;height:30px;border-radius:50%;background:var(--yellow)}
.lang{position:absolute;left:290px;top:48px;font-size:14px;color:#888}
.nav{position:absolute;right:146px;top:35px;display:flex;align-items:center;gap:22px}
.nav-home{background:var(--teal);color:#fff;font-size:15px;font-weight:500;padding:7px 26px;border-radius:18px}
.nav-item{color:#fff;font-size:15px;font-weight:500}
.hero-title{position:absolute;left:161px;top:258px;font-size:36px;line-height:45px;color:var(--ink);white-space:nowrap}
.btn{display:inline-block;border-radius:24px;text-transform:uppercase;text-align:center}
.btn-hero{position:absolute;left:161px;top:424px;width:198px;height:43px;line-height:43px;background:var(--teal);color:#fff;font-size:15px}
.slider-dots{position:absolute;left:559px;top:597px;display:flex;gap:8px}
.slider-dots span{width:22px;height:4px;border-radius:2px;border:1px solid #777}
.slider-dots .on{background:var(--teal);border-color:var(--teal)}

/* mssp band */
.mssp{position:absolute;left:0;top:631px;width:1200px;height:90px;background:var(--yellow)}
.mssp-text{position:absolute;left:161px;top:33px;font-size:19px;font-weight:600;color:var(--ink);letter-spacing:1px}
.btn-outline{position:absolute;left:889px;top:29px;width:150px;height:35px;line-height:33px;border:1.5px solid var(--ink);color:var(--ink);font-size:15px}

/* help */
.help-title{position:absolute;left:0;top:806px;width:1200px;text-align:center;font-size:45px;font-weight:600;color:var(--ink)}
.card{position:absolute;width:270px;background:#fff;box-shadow:0 2px 10px rgba(0,0,0,.12);text-align:center}
.card-head{height:212px;background:var(--dark);border-radius:135px 135px 0 0;color:#fff;font-size:17px;line-height:20px;padding:68px 40px 0}
.card-icon{position:absolute;left:68px;top:137px;width:134px;height:134px;border-radius:50%;background:#fff;display:flex;align-items:center;justify-content:center}
.card-body{padding:56px 22px 0}
.card-h{font-size:17px;line-height:22px;color:var(--ink);font-weight:500}
.card-p{margin-top:12px;font-size:13px;line-height:19.5px;color:var(--muted)}
.btn-card{position:absolute;left:45px;bottom:30px;width:180px;height:32px;line-height:32px;background:var(--dark);color:#fff;font-size:12px}
.btn-card.accent{background:var(--orange)}

/* trust */
.trust{position:absolute;left:0;top:1597px;width:1200px;height:463px;background:var(--soft)}
.trust-title{position:absolute;left:161px;top:80px;width:470px;font-size:27px;line-height:34px;color:var(--teal);letter-spacing:1px;white-space:nowrap}
.trust-p{position:absolute;left:161px;top:164px;width:440px;font-size:16.5px;line-height:22.5px;color:var(--text)}
.trust-h{position:absolute;left:161px;top:254px;font-size:18px;font-weight:500;color:var(--ink)}
.trust-small{position:absolute;left:161px;top:292px;width:440px;font-size:15px;line-height:22.5px;color:var(--text)}
.btn-trust{position:absolute;left:162px;top:354px;width:192px;height:39px;line-height:39px;background:var(--teal);color:#fff;font-size:14px}
.trust-photo{position:absolute;left:663px;top:81px;width:376px;height:295px;background:linear-gradient(135deg,#e9eaec 0%,#cfd2d6 45%,#545862 100%)}

/* clients */
.clients{position:absolute;left:188px;top:2137px;width:824px;height:200px;display:grid;grid-template-columns:repeat(4,1fr);grid-template-rows:repeat(2,1fr)}
.client{display:flex;align-items:center;justify-content:center;gap:8px;font-size:20px;font-weight:700;color:#3b3f47;position:relative}
.client:nth-child(-n+4){border-bottom:1px solid var(--line)}
.client:not(:nth-child(4n)):after{content:"";position:absolute;right:0;top:0;bottom:0;border-right:1px solid var(--line)}
.client-mark{width:14px;height:14px;background:#3b3f47}

/* footer */
.footer{position:absolute;left:0;top:2409px;width:1200px;height:414px;background:linear-gradient(100deg,var(--teal-dark) 0%,#1bbfc9 100%);color:#fff}
.f-col{position:absolute;top:62px}
.f-h{font-size:19px;font-weight:500;margin-bottom:18px}
.f-line{font-size:15px;line-height:24px;display:flex;gap:10px}
.f-line svg{flex:none;margin-top:3px}
.f-text{font-size:15px;line-height:24px}
.f-sep{position:absolute;top:62px;width:1px;height:160px;background:rgba(255,255,255,.7)}
.f-rule{position:absolute;left:160px;top:285px;width:878px;height:1px;background:rgba(255,255,255,.7)}
.f-brand{position:absolute;left:171px;top:320px;font-family:"Rajdhani",sans-serif;font-weight:700;font-size:18px;color:var(--ink)}
.f-rights{position:absolute;left:171px;top:349px;font-size:11px}
.badges{position:absolute;left:333px;top:310px;display:flex;gap:16px;align-items:center}
.badge{width:52px;height:52px;background:rgba(255,255,255,.35)}
.badge.round{border-radius:50%}
.to-top{position:absolute;left:1048px;top:273px;width:45px;height:45px;border-radius:50%;background:#fff;display:flex;align-items:center;justify-content:center}
</style>
</head>
<body>

<section class="hero">
  <div class="hero-photo" role="img" aria-label="Photo of a smiling woman holding a tablet in front of a glowing blue and purple network of padlock icons"></div>
  <svg class="hero-mask" width="1200" height="631" viewBox="0 0 1200 631" aria-hidden="true">
    <path d="M0 0H372C410 110 470 175 570 195C690 220 690 320 668 390C640 480 655 585 735 631H0Z" fill="#fff"/>
  </svg>
  <div class="brand"><span class="brand-dot"></span>Kestrel</div>
  <div class="lang">English ⌵</div>
  <nav class="nav">
    <span class="nav-home">Home</span>
    <span class="nav-item">Solution ⌵</span>
  </nav>
  <h1 class="hero-title display">TRAIN YOUR STAFF WITH<br>KESTREL AND IMPROVE CYBER<br>SECURITY AWARENESS</h1>
  <span class="btn btn-hero">Request a demo</span>
  <div class="slider-dots"><span class="on"></span><span></span><span></span></div>
</section>

<section class="mssp">
  <div class="mssp-text display">KESTREL IS ALSO AVAILABLE FOR MSSP</div>
  <span class="btn btn-outline">Learn more</span>
</section>

<h2 class="help-title">How Can We Help?</h2>

<article class="card" style="left:158px;top:918px;height:523px">
  <div class="card-head">Import our training courses in your LMS</div>
  <div class="card-icon">
    <svg width="86" height="86" viewBox="0 0 86 86" aria-hidden="true" fill="#16b5c2">
      <path d="M43 6 78 20 43 34 8 20Z"/><path d="M22 27v10c0 5 10 9 21 9s21-4 21-9V27L43 35Z"/>
      <rect x="8" y="52" width="11" height="28" rx="2"/>
      <path d="M23 54h22c6 0 6 8 0 8H33v3h14l22-12c6-3 10 4 5 8L50 78H23Z"/>
    </svg>
  </div>
  <div class="card-body">
    <div class="card-h">Buy out of the box or courses you can import in your elearning</div>
    <p class="card-p">Kestrel offers 250 fully customizable training modules in +30 Languages. Games, Videos, Exams, Posters,Offline, Micro-training and much more!</p>
  </div>
  <span class="btn btn-card">Explore our training</span>
</article>

<article class="card" style="left:465px;top:979px;height:522px">
  <div class="card-head" style="padding:60px 55px 0">Let us develop a security awareness program</div>
  <div class="card-icon">
    <svg width="80" height="90" viewBox="0 0 80 90" aria-hidden="true">
      <path d="M40 2 76 14V44C76 66 58 80 40 88 22 80 4 66 4 44V14Z" fill="#16b5c2"/>
      <circle cx="40" cy="44" r="18" fill="none" stroke="#fff" stroke-width="5"/>
      <path d="M31 44l7 7 12-13" fill="none" stroke="#fff" stroke-width="5" stroke-linecap="round" stroke-linejoin="round"/>
    </svg>
  </div>
  <div class="card-body">
    <div class="card-h">Kestrel security will assist you inimproving security awareness with money back guarantee!</div>
    <p class="card-p">Lorem Ipsum is simply dummy text of the printing and typesetting industry.</p>
  </div>
  <span class="btn btn-card accent">Explore our training</span>
</article>

<article class="card" style="left:768px;top:918px;height:523px">
  <div class="card-head" style="padding:62px 30px 0">Install the kestrel software on pemiseor get access to the saas vetsion</div>
  <div class="card-icon">
    <svg width="90" height="86" viewBox="0 0 90 86" aria-hidden="true" fill="#16b5c2">
      <rect x="37" y="2" width="16" height="26"/><path d="M22 28H68L45 52Z"/>
      <path d="M6 50 24 42 45 56 66 42 84 50 45 72Z"/><path d="M6 60 45 82 84 60 84 66 45 86 6 66Z"/>
    </svg>
  </div>
  <div class="card-body">
    <div class="card-h">You want to run the campaign yourself? Choose your perfered setup type and get started in 24h!</div>
    <p class="card-p">Lorem Ipsum is simply dummy text of the printing and typesetting industry. Lorem Ipsum</p>
  </div>
  <span class="btn btn-card">Explore our training</span>
</article>

<section class="trust">
  <h2 class="trust-title display">ALREADY OVER 12'000'000 EMPLOYEES<br>WORLDWIDE TRUST AND USE KESTREL</h2>
  <p class="trust-p">Kestrel Secure is a name you can trust! Because we have won countless awards since 2015 and help wellknown brands around the world.</p>
  <div class="trust-h">You know you're getting a quality solution with us.</div>
  <p class="trust-small">Our services can be customized to fit your needs and copany size. Talk to our team today to learn more</p>
  <span class="btn btn-trust">Contact with us</span>
  <div class="trust-photo" role="img" aria-label="Photo of a confident businesswoman in a dark suit with colleagues talking in an office behind her"></div>
</section>

<section class="clients" aria-label="Clients">
  <div class="client"><span class="client-mark"></span>Norvia</div>
  <div class="client">Railtek</div>
  <div class="client">Heimwert</div>
  <div class="client">Kornfeld</div>
  <div class="client">Alpair</div>
  <div class="client">Chemora</div>
  <div class="client">Vantrel</div>
  <div class="client" style="font-size:16px">Stadtwerk Nordhaven</div>
</section>

<footer class="footer">
  <div class="f-col" style="left:162px">
    <div class="f-h">Contact Us</div>
    <div class="f-line">
      <svg width="13" height="18" viewBox="0 0 13 18" aria-hidden="true"><path d="M6.5 0A6.5 6.5 0 0 0 0 6.5C0 11 6.5 18 6.5 18S13 11 13 6.5A6.5 6.5 0 0 0 6.5 0Zm0 9A2.5 2.5 0 1 1 6.5 4a2.5 2.5 0 0 1 0 5Z" fill="#fff"/></svg>
      <span>Uurope Kestrel Secure AG<br>Lindenweg 12 | 6400 Seeburg<br>Switzerland</span>
    </div>
    <div class="f-h" style="margin-top:32px;margin-left:-2px">Language</div>
    <div class="f-text" style="font-size:14px;margin-top:-10px">English ⌵</div>
  </div>
  <div class="f-sep" style="left:417px"></div>
  <div class="f-col" style="left:472px">
    <div class="f-h">Address</div>
    <div class="f-line">
      <svg width="13" height="18" viewBox="0 0 13 18" aria-hidden="true"><path d="M6.5 0A6.5 6.5 0 0 0 0 6.5C0 11 6.5 18 6.5 18S13 11 13 6.5A6.5 6.5 0 0 0 6.5 0Zm0 9A2.5 2.5 0 1 1 6.5 4a2.5 2.5 0 0 1 0 5Z" fill="#fff"/></svg>
      <span>North America<br>Kestrel Secure USA<br>4820 Harbor Loop Suite 210<br>Fairview, TX 70100</span>
    </div>
  </div>
  <div class="f-sep" style="left:756px"></div>
  <div class="f-col" style="left:807px">
    <div class="f-h">Phone</div>
    <div class="f-line" style="margin-bottom:14px"><svg width="17" height="17" viewBox="0 0 24 24" aria-hidden="true"><path d="M6.6 10.8a15 15 0 0 0 6.6 6.6l2.2-2.2c.3-.3.7-.4 1-.2 1.1.4 2.3.6 3.6.6.6 0 1 .4 1 1V20c0 .6-.4 1-1 1A17 17 0 0 1 3 4c0-.6.4-1 1-1h3.5c.6 0 1 .4 1 1 0 1.3.2 2.5.6 3.6.1.3 0 .7-.2 1Z" fill="#fff"/></svg><span>Global: +41 00 555 01 23</span></div>
    <div class="f-line" style="margin-bottom:14px"><svg width="17" height="17" viewBox="0 0 24 24" aria-hidden="true"><path d="M6.6 10.8a15 15 0 0 0 6.6 6.6l2.2-2.2c.3-.3.7-.4 1-.2 1.1.4 2.3.6 3.6.6.6 0 1 .4 1 1V20c0 .6-.4 1-1 1A17 17 0 0 1 3 4c0-.6.4-1 1-1h3.5c.6 0 1 .4 1 1 0 1.3.2 2.5.6 3.6.1.3 0 .7-.2 1Z" fill="#fff"/></svg><span>USA: +1 555 010 4411</span></div>
    <div class="f-line" style="margin-bottom:14px"><svg width="17" height="17" viewBox="0 0 24 24" aria-hidden="true"><path d="M6.6 10.8a15 15 0 0 0 6.6 6.6l2.2-2.2c.3-.3.7-.4 1-.2 1.1.4 2.3.6 3.6.6.6 0 1 .4 1 1V20c0 .6-.4 1-1 1A17 17 0 0 1 3 4c0-.6.4-1 1-1h3.5c.6 0 1 .4 1 1 0 1.3.2 2.5.6 3.6.1.3 0 .7-.2 1Z" fill="#fff"/></svg><span>USA Support: +1 555 010 4412</span></div>
    <div class="f-line"><svg width="17" height="17" viewBox="0 0 24 24" aria-hidden="true"><path d="M6.6 10.8a15 15 0 0 0 6.6 6.6l2.2-2.2c.3-.3.7-.4 1-.2 1.1.4 2.3.6 3.6.6.6 0 1 .4 1 1V20c0 .6-.4 1-1 1A17 17 0 0 1 3 4c0-.6.4-1 1-1h3.5c.6 0 1 .4 1 1 0 1.3.2 2.5.6 3.6.1.3 0 .7-.2 1Z" fill="#fff"/></svg><span>France: +33 555 010 778</span></div>
  </div>
  <div class="to-top"><svg width="14" height="9" viewBox="0 0 14 9" aria-hidden="true"><path d="M1 8l6-6 6 6" fill="none" stroke="#16b5c2" stroke-width="1.6"/></svg></div>
  <div class="f-rule"></div>
  <div class="f-brand">Kestrel</div>
  <div class="f-rights">All Rights Reserved 2020</div>
  <div class="badges" aria-label="Awards">
    <span class="badge round"></span><span class="badge round"></span><span class="badge"></span><span class="badge"></span><span class="badge"></span><span class="badge"></span><span class="badge"></span><span class="badge"></span><span class="badge round"></span><span class="badge round"></span>
  </div>
</footer>

</body>
</html>
```